Corvane Supplies Business Card

Professional business card that stand out to our potential customers. Front and back with clean modern design

Industry/Entity Type

Oil and gas

Contact Information for Business Card

Name, address, website , office phone and cell number

Requirements
Must have
• Editable files for each employee

```html
<!DOCTYPE html>
<html lang="en">
<head>
<meta charset="utf-8">
<title>Corvane Supplies Business Card</title>
<link rel="stylesheet" href="https://fonts.googleapis.com/css2?family=Roboto:wght@400;500;700&display=swap">
<style>
  :root {
    --backdrop: #3b3b3b;
    --card-black: #151515;
    --card-red: #b3080c;
    --card-red-dark: #8e0508;
    --accent-red: #ee1c24;
    --accent-blue: #1ab0d6;
    --white: #ffffff;
  }
  * { margin: 0; padding: 0; box-sizing: border-box; }
  html, body { width: 1200px; height: 694px; overflow: hidden; }
  body {
    background: var(--backdrop);
    font-family: "Roboto", Arial, sans-serif;
    position: relative;
  }
  .card {
    position: absolute;
    top: 197px;
    width: 520px;
    height: 300px;
    border-radius: 26px;
    overflow: hidden;
  }
  .card-front {
    left: 45px;
    background: var(--card-black);
    display: flex;
    align-items: center;
    justify-content: center;
  }
  .card-back {
    left: 635px;
    background: radial-gradient(ellipse at 40% 40%, var(--card-red), var(--card-red-dark));
    color: var(--white);
  }
  .brand {
    display: flex;
    align-items: center;
    gap: 12px;
  }
  .brand-mark {
    width: 22px;
    height: 22px;
  }
  .brand-name {
    font-weight: 700;
    text-transform: uppercase;
    letter-spacing: 1px;
  }
  .card-front .brand-mark { background: var(--accent-red); }
  .card-front .brand-name { color: var(--white); font-size: 34px; }
  .card-back .brand {
    position: absolute;
    left: 28px;
    top: 132px;
    width: 200px;
    flex-direction: column;
    gap: 10px;
  }
  .card-back .brand-mark { background: var(--white); width: 26px; height: 26px; }
  .card-back .brand-name {
    color: var(--white);
    font-size: 24px;
    text-align: center;
    line-height: 1.15;
  }
  .divider {
    position: absolute;
    left: 242px;
    top: 36px;
    width: 1.5px;
    height: 228px;
    background: var(--white);
  }
  .contact {
    position: absolute;
    left: 262px;
    top: 38px;
    right: 16px;
  }
  .person-name { font-size: 24px; font-weight: 500; line-height: 1.1; }
  .person-role { font-size: 13px; font-weight: 700; margin: 2px 0 12px 8px; }
  .address { font-size: 13px; line-height: 1.35; margin-bottom: 8px; }
  .contact-list { list-style: none; }
  .contact-list li {
    display: flex;
    align-items: flex-start;
    gap: 8px;
    font-size: 13px;
    line-height: 1.35;
    margin-bottom: 5px;
  }
  .contact-list svg { flex: 0 0 14px; width: 14px; height: 14px; margin-top: 2px; }
</style>
</head>
<body>
  <section class="card card-front">
    <div class="brand">
      <span class="brand-mark"></span>
      <span class="brand-name">Corvane Supplies</span>
    </div>
  </section>

  <section class="card card-back">
    <div class="brand">
      <span class="brand-mark"></span>
      <span class="brand-name">Corvane<br>Supplies</span>
    </div>
    <div class="divider"></div>
    <div class="contact">
      <div class="person-name">Dalen Whitcombe</div>
      <div class="person-role">Owner</div>
      <div class="address">412 N Harlan Rd Suite 5,<br>Midland, TX 79705, United States</div>
      <ul class="contact-list">
        <li>
          <svg viewBox="0 0 16 16" fill="#fff"><path d="M3 2h3l1 4-2 1a9 9 0 0 0 4 4l1-2 4 1v3a1 1 0 0 1-1 1A13 13 0 0 1 2 3a1 1 0 0 1 1-1z"/></svg>
          <span>(432)555-0187</span>
        </li>
        <li>
          <svg viewBox="0 0 16 16" fill="none" stroke="#fff" stroke-width="1.5"><rect x="1.5" y="3.5" width="13" height="9"/><path d="M1.5 3.5 8 9l6.5-5.5"/></svg>
          <span>sales@corvanesupplies.com</span>
        </li>
        <li>
          <svg viewBox="0 0 16 16" fill="none" stroke="#fff" stroke-width="1.4"><circle cx="8" cy="8" r="6.5"/><ellipse cx="8" cy="8" rx="2.8" ry="6.5"/><path d="M1.5 8h13"/></svg>
          <span>www.corvanesupplies.com</span>
        </li>
        <li>
          <svg viewBox="0 0 16 16" fill="none" stroke="#fff" stroke-width="1.5"><circle cx="8" cy="9" r="5.5"/><path d="M8 6v3l2 1.5M2 3l2-1.5M14 3l-2-1.5"/></svg>
          <span>Monday – Friday<br>8:30am – 5pm</span>
        </li>
      </ul>
    </div>
  </section>
</body>
</html>
```